Academic acomlishments and book promotional business card

Must Present my accomplishments in a strong fashion while looking very professional. We will need to make last minute changes in book title in about one to two months so it can't close until then. Must place a great emphasis on peer review. Treat this as if it were my business. It is more important than my titles. Vary fond slightly to emphasize peer review.
Updates

Project Deadline Extended
Reason: I will need to make small changes in book title in a month or two so it can't close until then.

Target Market(s)

Scholars, employers, patrons, and professionals.

Industry/Entity Type

Business

Contact Information for Business Card

Basic content:

Miles T. Brenvorth
Peer review by: Halbrook University Press + Quellmark Books + F. K. Ravell Co. + Edgar Fennick & Sons

Evolutionary Scientist + Historian

Academic Consultant, Marlowe University Press

See Overleaf

quillmiles@mailbrook.com + Cell. (555) 218-7634

Reverse Side:

In the distant future I see open fields for far more important researches. Psychology will be based on a new foundation, that of the necessary squire Kent of each mental power by gradation. Light will be thrown on the origin of man and his history. --Henry Lowcastle [make dash one line]

Book: "Tribal Debt or Civic Debt: Adaptive Behaviour,..."

See Folioface for CV with Endorsements + Writing Sample.

Font styles to use
Serif

Requirements
Must have
• The font has to be big enough etc to be able to use the gold ink at printvela.com, who will print them. Pls see their website for specs.
Nice to have
• Have a capital of the last letter in the Greek alphabet as a decorative element. Though this is not necessary.
Should not have
• Not Ornate or very curvalinear font.

```html
<!DOCTYPE html>
<html lang="en">
<head>
<meta charset="utf-8">
<title>Miles T. Brenvorth — Business Card</title>
<link rel="stylesheet" href="https://fonts.googleapis.com/css2?family=EB+Garamond:wght@400;500;600;700&display=swap">
<style>
  :root {
    --backdrop: #ececec;
    --card: #ffffff;
    --brand-blue: #1f72bb;
    --band-blue: #2a7cc4;
    --ink: #4a4a4a;
    --on-blue: #ffffff;
  }
  * { margin: 0; padding: 0; box-sizing: border-box; }
  html, body {
    width: 1200px; height: 800px; overflow: hidden;
    background: var(--backdrop);
    font-family: "EB Garamond", Georgia, serif;
    color: var(--ink);
  }
  .stage {
    position: relative; width: 1200px; height: 800px;
    display: flex; align-items: center; justify-content: center; gap: 40px;
  }
  .card {
    position: relative; width: 560px; height: 320px;
    background: var(--card);
    box-shadow: 0 2px 8px rgba(0,0,0,0.12);
    overflow: hidden;
  }
  .rule { position: absolute; left: 0; right: 0; height: 5px; background: var(--brand-blue); }
  .band {
    position: absolute; left: 0; right: 0;
    background: var(--band-blue); color: var(--on-blue);
    text-align: center;
    display: flex; flex-direction: column; justify-content: center;
  }

  /* Back side */
  .card--back .rule--top { top: 14px; }
  .card--back .band { top: 24px; height: 72px; }
  .card--back .rule--under { top: 101px; }
  .book-label { font-size: 19px; font-weight: 600; line-height: 1.2; }
  .book-title { font-size: 19px; font-weight: 600; line-height: 1.25; }
  .quote {
    position: absolute; top: 122px; left: 34px; right: 30px;
    list-style: none; font-size: 15px; font-weight: 500; line-height: 1.35;
  }
  .quote li { padding-left: 10px; text-indent: -10px; }
  .quote li::before { content: "- "; }
  .attribution {
    position: absolute; top: 228px; left: 0; right: 0;
    text-align: center; color: var(--brand-blue); font-size: 15px; font-weight: 500;
  }
  .overleaf-note {
    position: absolute; top: 268px; left: 0; right: 0;
    text-align: center; font-size: 15px; font-weight: 500;
  }

  /* Front side */
  .identity { position: absolute; top: 40px; left: 40px; }
  .name { color: var(--brand-blue); font-size: 24px; font-weight: 700; line-height: 1.2; margin-bottom: 8px; }
  .role { font-size: 16px; font-weight: 500; line-height: 1.3; }
  .contact { position: absolute; top: 130px; left: 40px; font-size: 16px; font-weight: 600; line-height: 1.3; }
  .contact dt { display: inline-block; width: 50px; }
  .contact dd { display: inline; }
  .card--front .rule--over { top: 208px; }
  .card--front .band { top: 220px; height: 64px; }
  .card--front .rule--bottom { top: 292px; height: 6px; }
  .peer-heading { font-size: 20px; font-weight: 700; line-height: 1.2; margin-bottom: 4px; }
  .peer-list { font-size: 14px; font-weight: 400; line-height: 1.2; }
</style>
</head>
<body>
<main class="stage">

  <section class="card card--back" aria-label="Card reverse side">
    <div class="rule rule--top"></div>
    <div class="band">
      <p class="book-label">Book :</p>
      <p class="book-title">"Tribal Debt or Civic Debt: Adaptive Behaviour,..."</p>
    </div>
    <div class="rule rule--under"></div>
    <ul class="quote">
      <li>In the distant future I see open fields for far more important researches.</li>
      <li>Psychology will be based on a new foundation, that of the necessary squire Kent of each mental power by gradation.</li>
      <li>Light will be thrown on the origin of man and his history.</li>
    </ul>
    <p class="attribution">–Henry Lowcastle</p>
    <p class="overleaf-note">See Folioface for CV with Endorsements + Writing Sample.</p>
  </section>

  <section class="card card--front" aria-label="Card front side">
    <div class="identity">
      <h1 class="name">Miles T. Brenvorth</h1>
      <p class="role">Evolutionary Scientist + Historian</p>
      <p class="role">Academic Consultant, Marlowe University Press</p>
    </div>
    <dl class="contact">
      <div><dt>Cell</dt><dd>: (555) 218-7634</dd></div>
      <div><dt>Email</dt><dd>: quillmiles@mailbrook.com</dd></div>
    </dl>
    <div class="rule rule--over"></div>
    <div class="band">
      <p class="peer-heading">Peer review by :</p>
      <p class="peer-list">Halbrook University Press + Quellmark Books + F. K. Ravell Co. + Edgar Fennick &amp; Sons.</p>
    </div>
    <div class="rule rule--bottom"></div>
  </section>

</main>
</body>
</html>
```